Vorn Solutions: searching for a flyer to trow in letterboxes for properties we are interested in

Hello ,

Introduction:
We are a company based in Luxembourg called "Vorn Solutions". We are specialized in buying properties on which we develop and build constructions before selling them.

Informations for the flyer:
We need a flyer to trow into the letter boxes of property owners letting them know that we are interested in buying their property, if they are interested they can give us a call.

The text for the flyer/letter is in the attachment called >>2020-03-11_VS_Text for flyer,letter there might be slight changes<<.

We need to look competent, professional and financially stable.

The flyer needs to be short and not over welling with information otherwise it will land in the trash.

We have decided that we don't want real pictures on the flyer, but shapes of any kind, blue prints, drawings are fine.

Format should be in DIN A4. We plan to print the flyer on both sides in two different languages, in other words the design will be the same on both sides only the text will be in a different language.

I also added our current logo and here is the design of the website that is under construction at the moment http://www.vornsolutions.example/. The logo's color can be changed into a different blue or uni color (all white or all black).
Updates

Hi, First time user the howl thing started faster as expected. Furthermore, I need to catch my boss to discust the project with him and he is on a lot of meetings. Please give us a little bit more time. Thanks

Target Market(s)

Property owners

Requirements
Must have
• email, phone number, tax number (RCS), Tax number , matriculation and address.
see word file in attachment for information
Nice to have
• Our company logo, in one form or an other, you can be creative, the logo is in the attachment.
Should not have
• Real pictures

```html
<!DOCTYPE html>
<html lang="fr">
<head>
<meta charset="utf-8">
<title>Vorn Solutions – Flyer</title>
<link rel="stylesheet" href="https://fonts.googleapis.com/css2?family=Exo+2:wght@500&family=Lato:ital,wght@0,700;1,400&display=swap">
<style>
  :root {
    --navy: #0a4670;
    --blue: #0b6694;
    --title-blue: #0e5f8f;
    --light-blue: #a3c7da;
    --paper: #ffffff;
    --paper-tint: #e9f1f8;
    --ink: #222222;
    --backdrop: #d9dcdf;
  }
  * { margin: 0; padding: 0; box-sizing: border-box; }
  html, body { width: 1200px; height: 1200px; overflow: hidden; background: var(--backdrop); }
  .flyer {
    position: absolute; left: 190px; top: 20px;
    width: 905px; height: 1280px;
    transform: scale(0.906); transform-origin: top left;
    background: linear-gradient(180deg, var(--paper) 35%, var(--paper-tint) 100%);
    box-shadow: 0 6px 18px rgba(0,0,0,.25);
    overflow: hidden;
  }
  .header {
    position: absolute; left: 0; top: 0; width: 905px; height: 431px;
    background: linear-gradient(120deg, #093f63 0%, var(--navy) 45%, #0d6899 100%);
  }
  .rcs-tab { position: absolute; right: 0; top: 0; width: 235px; height: 36px; }
  .rcs-label {
    position: absolute; left: 727px; top: 8px;
    font: 500 17px "Exo 2", sans-serif; color: var(--navy);
  }
  .wordmark {
    position: absolute;
    font: 500 34px/1 "Exo 2", sans-serif; letter-spacing: 0;
  }
  .wordmark--header { left: 0; width: 905px; top: 215px; text-align: center; color: #fff; }
  .wordmark--footer { right: 35px; top: 1046px; text-align: right; font-size: 30px; color: var(--navy); }
  .tagline {
    position: absolute; left: 0; top: 324px; width: 905px; text-align: center;
    font-family: "Exo 2", sans-serif; font-weight: 500; color: #fff; line-height: 30px;
  }
  .tagline__main { font-size: 28px; display: block; }
  .tagline__sub { font-size: 27px; display: block; }
  .tagline-rule {
    position: absolute; left: 312px; top: 395px; width: 280px;
    border-top: 3px dotted rgba(255,255,255,.8);
  }
  .letter { position: absolute; left: 38px; top: 472px; width: 850px; }
  .letter p { font: italic 400 20px/25px "Lato", sans-serif; color: var(--ink); margin-bottom: 26px; }
  .letter .salutation { font: 700 20px/25px "Lato", sans-serif; color: var(--title-blue); margin-bottom: 26px; }
  .letter .closing { font: 700 20px/25px "Lato", sans-serif; color: var(--ink); margin-top: 52px; }
  .letter .signature { font: 700 20px/25px "Lato", sans-serif; color: var(--title-blue); }
  .footer-shapes { position: absolute; left: 0; top: 0; width: 905px; height: 1280px; }
  .contact {
    position: absolute; left: 245px; top: 1097px;
    list-style: none; font: 500 19px/24px "Exo 2", sans-serif; color: #fff;
  }
  .contact li { display: flex; align-items: center; gap: 8px; }
  .contact .icon { width: 17px; height: 17px; flex: none; }
  .contact .company { padding-left: 25px; }
  .website {
    position: absolute; left: 240px; top: 1213px;
    display: flex; align-items: center; gap: 10px;
    font: 500 25px/30px "Exo 2", sans-serif; color: var(--title-blue);
  }
</style>
</head>
<body>
<article class="flyer">
  <header class="header" role="img" aria-label="Blueprint-style scaffolding line drawing on a deep blue background"></header>
  <svg class="rcs-tab" viewBox="0 0 235 36" aria-hidden="true"><polygon points="0,0 235,0 235,36 38,36" fill="#fff"/></svg>
  <span class="rcs-label">RCS:</span>
  <div class="wordmark wordmark--header">Vorn Solutions</div>
  <p class="tagline">
    <span class="tagline__main">WE ARE SPECIALIZED IN BUYING PROPERTIES</span>
    <span class="tagline__sub">on which we develop and build constructions before selling them</span>
  </p>
  <div class="tagline-rule"></div>

  <section class="letter">
    <p class="salutation">Madame, Monsieur,</p>
    <p>Ce courrier vous a été adressé, car votre propriété a attiré notre attention.<br>Nous souhaiterions discuter avec vous de son éventuel rachat par notre société.</p>
    <p>En cas d’accord, nous vous assurons une décision rapide, un paiement garanti,<br>et zéro frais d’intermédiaire.</p>
    <p>En attendant de vos nouvelles, nous restons à votre entière disposition pour tout renseignement.</p>
    <p class="closing">Salutations distinguées,</p>
    <p class="signature">L’équipe de Vorn Solutions</p>
  </section>

  <svg class="footer-shapes" viewBox="0 0 905 1280" aria-hidden="true">
    <polygon points="0,1083 222,923 222,1048 0,1203" fill="var(--blue)"/>
    <polygon points="0,1086 905,1086 770,1203 0,1203" fill="var(--navy)"/>
    <polygon points="905,1098 905,1203 842,1148" fill="var(--light-blue)"/>
  </svg>

  <div class="wordmark wordmark--footer">Vorn Solutions</div>

  <ul class="contact">
    <li class="company">Vorn Solutions sàrl</li>
    <li><svg class="icon" viewBox="0 0 16 16"><path d="M8 1a5 5 0 0 0-5 5c0 4 5 9 5 9s5-5 5-9a5 5 0 0 0-5-5zm0 7a2 2 0 1 1 0-4 2 2 0 0 1 0 4z" fill="#fff"/></svg>18 rue des Ateliers, L-4410 Soleuvre</li>
    <li><svg class="icon" viewBox="0 0 16 16"><rect x="1.5" y="3.5" width="13" height="9" fill="none" stroke="#fff" stroke-width="1.3"/><path d="M1.5 3.5 8 9l6.5-5.5" fill="none" stroke="#fff" stroke-width="1.3"/></svg>info@vornsolutions.example</li>
    <li><svg class="icon" viewBox="0 0 16 16"><path d="M4 1.5 6.3 4 5 5.8c.8 1.9 2.3 3.4 4.2 4.2L11 8.7l2.5 2.3-1.4 2.7C7 13.5 2.5 9 2.3 3.9z" fill="#fff"/></svg>691 000 482</li>
  </ul>

  <div class="website">
    <svg width="22" height="22" viewBox="0 0 22 22" aria-hidden="true"><g fill="none" stroke="var(--title-blue)" stroke-width="1.8"><circle cx="11" cy="11" r="9"/><ellipse cx="11" cy="11" rx="4" ry="9"/><path d="M2 11h18M4 6h14M4 16h14"/></g></svg>
    <span>WWW.VORNSOLUTIONS.EXAMPLE</span>
  </div>
</article>
</body>
</html>
```